(Wordpress)Website Design - No requirements! Sign Your name at the bottom of the site!

Dear Designer,

I am looking for a designer who is interested in a long-term business realtionship.
I already have 2 more designs to get done IMMEDIATELY after this website..
1.) An email brochure matching the website theme.
2.) A Billboard. BOTH MATCHING THE WEBSITE THEME

For this project, a bonus WILL be given.

Go to vaultnest.com as Site Inspiration

Please take this opportunity to design an existing wordpress website, FUNDSWIFTLANE.com, in whatever form your creativity takes you

I have no requirements other than a CREATIVE and OUT-OF -THE-BOX Design. Something Pretty and Eye Catching; a website that someone logs onto and doesnt want to leave

I have purchased a theme called velorant. You dont need to use it...But Info can be found at

http://skinbazaar.example/item/velorant-premium-wordpress-theme/full_screen_preview/482715

I have attached my logos and a PDF with a short story about what our company does.

Thank You,
-Tobin
PS I HAVE ANOTHER 2 DESIGNS TO DO AFTER THIS PROJECT.
also, IF YOU KNOW OF SOMEONE WHO DOES SEO WORK, I AM LOOKING FOR A FULL-TIME EMPLOYEE

Target Market(s)

Business Owners in a state of finacial NEED

Industry/Entity Type

Business

Requirements
Must have
• COLORFUL, EYE CATCHING

```html
<!DOCTYPE html>
<html lang="en">
<head>
<meta charset="utf-8">
<title>Swiftlane Capital</title>
<link href="https://fonts.googleapis.com/css2?family=Comfortaa:wght@400;700&family=Ubuntu:wght@400;500&family=Arimo:wght@400;700&display=swap" rel="stylesheet">
<style>
  :root {
    --paper: #f1ebe7;
    --paper-edge: #e4dcd6;
    --ink: #333333;
    --ink-soft: #4a4a4a;
    --sky-top: #0a7fb5;
    --sky-mid: #4ba3c9;
    --sky-low: #86bfd8;
    --call-top: #b6dc2a;
    --call-bottom: #8cc414;
    --btn-frame: #7f8c93;
    --btn-top: #6ccbff;
    --btn-bottom: #1795f0;
    --orange: #e9530f;
    --orange-light: #ff9a2a;
    --dot: #8a8a8a;
    --white: #ffffff;
  }
  * { margin: 0; padding: 0; box-sizing: border-box; }
  html, body {
    width: 1200px; height: 1061px; overflow: hidden;
    background: var(--paper);
    font-family: "Arimo", Arial, sans-serif;
  }
  .page { position: relative; width: 1200px; height: 1061px; background: var(--paper); }

  .site-header { position: absolute; top: 0; left: 0; width: 1200px; height: 82px; }
  .brand {
    position: absolute; left: 88px; top: 20px;
    display: flex; align-items: center; gap: 10px;
    font-family: "Ubuntu", sans-serif; font-size: 34px; font-weight: 400;
    color: #3d6fb5; letter-spacing: -0.5px;
  }
  .brand-mark { width: 34px; height: 34px; border-radius: 50%; background: #6f9a5a; }
  .main-nav { position: absolute; top: 0; left: 528px; height: 82px; display: flex; align-items: center; }
  .main-nav a {
    color: var(--ink); text-decoration: none; font-size: 15px;
    padding: 0 17px; height: 46px; line-height: 46px;
    border-right: 1px solid #dcd3cd;
  }
  .main-nav a:last-child { border-right: none; }
  .call-tab {
    position: absolute; left: 998px; top: 0; width: 157px; height: 95px;
    background: linear-gradient(var(--call-top), var(--call-bottom));
    clip-path: polygon(0 0, 100% 0, 100% 100%, 50% 92%, 0 100%);
    text-align: center; color: var(--white);
  }
  .call-tab .call-label { font-family: "Ubuntu", sans-serif; font-size: 24px; margin-top: 10px; }
  .call-tab .call-number { font-size: 17px; margin-top: 6px; }

  .hero {
    position: absolute; top: 82px; left: 0; width: 1200px; height: 483px;
    border-top: 1px solid #9fc7da; border-bottom: 2px solid #d8e8ef;
    overflow: hidden;
  }
  .hero-art {
    position: absolute; inset: 0;
    background:
      radial-gradient(ellipse 420px 380px at 600px 160px, rgba(255,255,255,0.22), transparent 70%),
      linear-gradient(180deg, var(--sky-top) 0%, var(--sky-mid) 55%, var(--sky-low) 100%);
  }
  .hero-title {
    position: absolute; left: 0; width: 1230px; top: 70px; text-align: center;
    font-family: "Comfortaa", sans-serif; font-weight: 700; font-size: 46px; color: var(--white);
  }
  .hero-lede {
    position: absolute; left: 304px; top: 162px; width: 620px;
    font-family: "Ubuntu", sans-serif; font-size: 31px; line-height: 38.7px; color: var(--white);
  }
  .hero-button-frame {
    position: absolute; left: 448px; top: 360px; width: 321px; height: 92px;
    background: var(--btn-frame); border-radius: 7px;
    box-shadow: inset 0 1px 0 rgba(255,255,255,0.3), 0 2px 4px rgba(0,0,0,0.25);
  }
  .hero-button {
    position: absolute; left: 22px; top: 17px; width: 277px; height: 60px;
    background: linear-gradient(var(--btn-top) 0%, #3fb3fb 50%, var(--btn-bottom) 51%, var(--btn-bottom) 100%);
    border-radius: 5px; color: var(--white); text-decoration: none;
    font-family: "Ubuntu", sans-serif; font-size: 38px; line-height: 60px; text-align: center;
  }

  .slider-dots { position: absolute; top: 579px; left: 583px; display: flex; gap: 9px; }
  .slider-dots span { width: 10px; height: 10px; border-radius: 50%; background: var(--dot); box-shadow: inset 0 1px 2px rgba(0,0,0,0.4); }
  .slider-dots span.active { background: var(--orange); }
  .scroll-arrow { position: absolute; left: 589px; top: 600px; }
  .timeline-line { position: absolute; left: 618px; top: 667px; height: 175px; border-left: 1px dashed #222; }

  .section-heading { position: absolute; left: 529px; top: 848px; width: 178px; text-align: center; color: var(--ink-soft); }
  .section-heading .small { font-family: "Comfortaa", sans-serif; font-size: 16px; display: block; }
  .ribbon { position: relative; height: 74px; margin-top: 6px; }
  .ribbon .ribbon-text {
    position: absolute; left: 0; right: 0; top: 22px;
    font-family: "Comfortaa", sans-serif; font-weight: 700; font-size: 22px; color: var(--white);
    transform: rotate(-6deg);
  }
  .section-heading .big { font-weight: 700; font-size: 37px; color: #3f3f3f; display: block; margin-top: -4px; }
</style>
</head>
<body>
<div class="page">
  <header class="site-header">
    <div class="brand"><span class="brand-mark"></span>Swiftlane Capital</div>
    <nav class="main-nav">
      <a href="#">About</a>
      <a href="#">Success Stories</a>
      <a href="#">Apply</a>
      <a href="#">Swiftlane Charity</a>
    </nav>
    <div class="call-tab">
      <div class="call-label">CALL US</div>
      <div class="call-number">(888) 555-0142</div>
    </div>
  </header>

  <section class="hero">
    <div class="hero-art" role="img" aria-label="Blue sky over clouds with large curling banknotes and small groups of business people standing on them"></div>
    <h1 class="hero-title">Welcome to Swiftlane Capital</h1>
    <p class="hero-lede">We are a funding agency helping business like you get the money they need.<br>We go above and beyond searhing for the best deal for you.</p>
    <div class="hero-button-frame"><a class="hero-button" href="#">About</a></div>
  </section>

  <div class="slider-dots"><span></span><span></span><span class="active"></span><span></span></div>
  <svg class="scroll-arrow" width="56" height="56" viewBox="0 0 56 56" aria-hidden="true">
    <circle cx="28" cy="28" r="27" fill="#ffffff" stroke="#e6ddd7"/>
    <circle cx="28" cy="28" r="22" fill="#f26a12"/>
    <circle cx="28" cy="24" r="18" fill="#ff9a2a" opacity="0.5"/>
    <path d="M23 16h10v12h7L28 41 16 28h7z" fill="#ffffff"/>
  </svg>
  <div class="timeline-line"></div>

  <div class="section-heading">
    <span class="small">The</span>
    <div class="ribbon">
      <svg width="178" height="74" viewBox="0 0 178 74" aria-hidden="true">
        <path d="M0 24 L178 4 L178 52 L0 72 Z" fill="#e4500e"/>
        <path d="M4 38h14M4 46h14M4 54h14M160 22h14M160 30h14M160 38h14" stroke="#ffffff" stroke-width="2"/>
      </svg>
      <span class="ribbon-text">DILEMMA</span>
    </div>
    <span class="small">We Are</span>
    <span class="big">Facing</span>
  </div>
</div>
</body>
</html>
```